Flyer for a marketing

We are a holistic mental health facility in need of a flyer to help promote our services and encourage more people to seek care. See the attachment to tell you more. We prefer warm green colors or rich blue. Thank you.

```html
<!DOCTYPE html>
<html lang="en">
<head>
<meta charset="utf-8">
<title>Evergreen Mind Health and Wellness – Flyer</title>
<link href="https://fonts.googleapis.com/css2?family=Montserrat:ital,wght@0,400;0,500;0,700;0,800;1,800&display=swap" rel="stylesheet">
<style>
  :root{
    --backdrop:#a7c5c7;
    --paper:#ffffff;
    --ink-headline:#22344c;
    --ink:#1e3a63;
    --footer:#1e4068;
    --band-light:#9fe0f3;
    --band-mid:#2c7fa6;
    --accent:#40c4ea;
    --photo-dark:#1d2a33;
    --photo-light:#b9cfd6;
  }
  *{margin:0;padding:0;box-sizing:border-box}
  html,body{width:1008px;height:1200px;overflow:hidden;background:var(--backdrop);font-family:"Montserrat",sans-serif;color:var(--ink)}
  .flyer{position:absolute;left:166px;top:122px;width:676px;height:954px;background:var(--paper);overflow:hidden}
  .abs{position:absolute}

  .brand-mark{left:82px;top:75px;width:50px;height:50px;border-radius:50%;background:var(--accent)}
  .brand-rule{left:177px;top:37px;width:2px;height:116px;background:var(--ink)}
  .brand-name{left:196px;top:56px;font-size:14px;line-height:19px;font-weight:500;text-transform:uppercase;letter-spacing:.06em;color:var(--ink)}
  .tagline{left:64px;top:160px;font-size:18px;font-weight:400;letter-spacing:.02em;color:var(--ink)}

  .hero-photo{left:282px;top:39px;width:358px;height:414px}

  .headline{left:61px;top:222px;font-size:51px;line-height:59px;font-weight:800;letter-spacing:-.015em;white-space:nowrap;color:var(--ink-headline);
    -webkit-text-stroke:6px var(--paper);paint-order:stroke fill}

  .offer{left:0;width:676px;top:494px;text-align:center;font-size:28px;line-height:32px;font-weight:800;font-style:italic;color:var(--ink)}
  .invite{left:0;width:676px;top:578px;text-align:center;font-size:16.5px;line-height:28px;font-weight:500;color:var(--ink)}
  .invite strong{font-size:25px;font-weight:800;margin-right:6px}
  .why{left:0;width:676px;top:650px;text-align:center;font-size:13.4px;line-height:17.6px;font-weight:500;letter-spacing:.02em;color:var(--ink)}
  .why h2{font-size:13.4px;font-weight:800;margin-bottom:2px}
  .why .promise{font-weight:800;margin-top:17px;line-height:16px}

  .band-light{left:0;top:807px;width:676px;height:10px;background:var(--band-light)}
  .band-mid{left:0;top:817px;width:676px;height:10px;background:var(--band-mid)}
  .footer{left:0;top:827px;width:676px;height:127px;background:var(--footer);color:var(--paper)}
  .footer-rule{left:291px;top:3px;width:1px;height:112px;background:var(--paper)}
  .contact{display:flex;align-items:center;gap:12px;font-weight:800;white-space:nowrap}
  .phone{left:36px;top:27px;font-size:18.5px}
  .fax{left:36px;top:71px;font-size:18.5px}
  .address{left:308px;top:17px;font-size:11px;line-height:13px}
  .email{left:308px;top:52px;font-size:15.5px;gap:8px}
  .web{left:308px;top:79px;font-size:15.5px;gap:8px}
  .contact svg{flex:none}
</style>
</head>
<body>
<main class="flyer">
  <span class="abs brand-mark"></span>
  <span class="abs brand-rule"></span>
  <div class="abs brand-name">Evergreen<br>Mind<br>Health<br>and<br>Wellness</div>
  <p class="abs tagline">The Care You Deserve</p>

  <svg class="abs hero-photo" viewBox="0 0 358 414" role="img" aria-label="Photo of a person sitting alone on a hallway floor, head resting on knees, in cool blue tones">
    <defs>
      <linearGradient id="photoTone" x1="0" y1="0" x2="1" y2="0.3">
        <stop offset="0" stop-color="var(--photo-dark)"/>
        <stop offset="0.55" stop-color="#4d6470"/>
        <stop offset="1" stop-color="var(--photo-light)"/>
      </linearGradient>
    </defs>
    <path d="M150 12 Q179 -12 208 12 L346 172 Q370 207 346 242 L208 402 Q179 426 150 402 L12 242 Q-12 207 12 172 Z" fill="url(#photoTone)"/>
  </svg>

  <h1 class="abs headline">where<br>deserving patients<br>meet compassionate<br>providers.</h1>

  <p class="abs offer">We are accepting new patients,<br>no waiting list.</p>
  <p class="abs invite">Your mental health matters, so make it a priority and<br><strong>call us today</strong> for an appointment.</p>

  <section class="abs why">
    <h2>Why choose us?</h2>
    <p>We are an integrative holistic psychiatric center.<br>Our mission is to provide compassionate quality care.<br>We provide psychiatric services including medication<br>management and psychotherapy.</p>
    <p class="promise">We listen, care, and empower you to live better.<br>We accept major insurances.</p>
  </section>

  <span class="abs band-light"></span>
  <span class="abs band-mid"></span>
  <footer class="abs footer">
    <span class="abs footer-rule"></span>
    <div class="abs contact phone">
      <svg width="24" height="24" viewBox="0 0 24 24" fill="none" stroke="currentColor" stroke-width="1.6"><circle cx="12" cy="12" r="11"/><path d="M8 6.5l2 2.2-1.2 1.6c.8 1.8 2.2 3.2 4 4l1.6-1.2 2.2 2-1.3 1.9C10.8 16.8 7.2 13.2 6.1 8z" fill="currentColor" stroke="none"/></svg>
      <span>Ph (555) 014-2738</span>
    </div>
    <div class="abs contact fax">
      <svg width="24" height="24" viewBox="0 0 24 24" fill="currentColor"><rect x="6" y="2" width="12" height="6" rx="1"/><rect x="2" y="8" width="20" height="9" rx="2"/><rect x="6" y="14" width="12" height="8" rx="1" fill="var(--footer)" stroke="currentColor" stroke-width="1.8"/><rect x="8.5" y="17" width="7" height="1.4"/></svg>
      <span>Fax (555) 019-6604</span>
    </div>
    <div class="abs contact address">
      <svg width="18" height="24" viewBox="0 0 18 24"><path d="M9 1a8 8 0 0 0-8 8c0 6 8 14 8 14s8-8 8-14a8 8 0 0 0-8-8z" fill="currentColor"/><circle cx="9" cy="9" r="3" fill="var(--footer)"/></svg>
      <span>Evergreen Mind Health and Wellness, APNC<br>4180 Harbor View Road, Suite 200 Lakeside, CA 90210</span>
    </div>
    <div class="abs contact email">
      <svg width="18" height="14" viewBox="0 0 18 14" fill="none" stroke="currentColor" stroke-width="1.5"><rect x="1" y="1" width="16" height="12" rx="1.5"/><path d="M1.5 2l7.5 6 7.5-6"/></svg>
      <span>info@evergreenmindhealth.com</span>
    </div>
    <div class="abs contact web">
      <svg width="18" height="18" viewBox="0 0 18 18" fill="none" stroke="currentColor" stroke-width="1.3"><circle cx="9" cy="9" r="7.5"/><ellipse cx="9" cy="9" rx="3.2" ry="7.5"/><path d="M1.5 9h15M2.5 5.3h13M2.5 12.7h13"/></svg>
      <span>evergreenmindhealth.com</span>
    </div>
  </footer>
</main>
</body>
</html>
```